Crisp vintage hair . Need to be noticed small town with 15 other salons which are all clinical clean

Hair salon, modern industrial look, new image face lift, been an established salon for 35+ years was extremely dated (80s) need to be known as successful fresh look salon.
All aspects of hair- ladies mens and children, style cuts, basic - fashion colour work, blowdry, Upstyling, perming, hair treatments, professional color and retail. Specialising staff for color and cuts. Staff ages young and funky to mature
Updates

Reason: Would like some more variety of design

Target Market(s)

Walk by traffic, new clients, to be seen

Industry/Entity Type

Hair

Font styles to use
Sans Serif

Requirements
Must have
• Crisp vintage hair
Nice to have
• Timber look, brick
Should not have
• Pretty (floral, script writing , pictures of sissors or combs or brushes)

```html
<!DOCTYPE html>
<html lang="en">
<head>
<meta charset="utf-8">
<title>Crisp Vintage Hair – Shopfront</title>
<link rel="stylesheet" href="https://fonts.googleapis.com/css2?family=Oswald:wght@400;500;600&display=swap">
<style>
  :root {
    --timber-light: #f0d4b4;
    --timber-mid: #e4bf98;
    --timber-grain: #d9ad82;
    --ink: #000000;
    --brass: #e6b98f;
    --paper: #ffffff;
    --glass-warm: #6b5440;
    --glass-deep: #2a2320;
  }
  * { margin: 0; padding: 0; box-sizing: border-box; }
  html, body { width: 1200px; height: 849px; overflow: hidden; background: var(--paper); }
  body { font-family: "Oswald", "Arial Narrow", sans-serif; position: relative; }

  .shopfront { position: absolute; inset: 0; }

  .timber {
    background:
      repeating-linear-gradient(90deg, transparent 0 118px, rgba(185,140,95,.25) 118px 120px),
      repeating-linear-gradient(180deg, var(--timber-light) 0 9px, var(--timber-mid) 9px 14px, var(--timber-light) 14px 22px, var(--timber-grain) 22px 24px);
  }

  .fascia { position: absolute; left: 42px; top: 184px; width: 1090px; height: 114px; }
  .fascia-band {
    position: absolute; left: 261px; top: 210px; width: 651px; height: 64px;
    background: var(--ink); display: flex; align-items: center;
  }
  .fascia-dot {
    width: 44px; height: 44px; border-radius: 50%; background: var(--brass);
    margin-left: 110px; flex: none;
  }
  .fascia-name {
    color: var(--brass); font-weight: 500; font-size: 50px; line-height: 1;
    margin-left: 70px; letter-spacing: .5px;
  }

  .pillar { position: absolute; left: 42px; top: 298px; width: 124px; height: 322px; }
  .pillar-name {
    position: absolute; left: 42px; top: 330px; width: 124px; text-align: center;
    color: var(--ink); font-weight: 600; font-size: 19px; line-height: 1.05; text-transform: uppercase;
  }
  .service-list {
    position: absolute; left: 70px; top: 398px; width: 64px; height: 192px;
    background: var(--ink); list-style: none; padding-top: 22px;
    display: flex; flex-direction: column; align-items: center;
  }
  .service-list li { color: var(--brass); font-size: 11.5px; line-height: 16px; letter-spacing: 1px; }

  .frame { position: absolute; left: 166px; top: 298px; width: 926px; height: 316px; background: var(--ink); }
  .frame-text { position: absolute; top: 326px; color: var(--paper); font-size: 18px; letter-spacing: .5px; }
  .frame-text.phone { left: 186px; }
  .frame-text.web { left: 581px; }

  .window { position: absolute; background: linear-gradient(180deg, var(--glass-warm), var(--glass-deep)); }
  .window.left { left: 166px; top: 356px; width: 314px; height: 248px; }
  .window.right { left: 570px; top: 358px; width: 424px; height: 250px; }
  .window-band {
    position: absolute; height: 14px; background: var(--paper);
  }
  .window.left .window-band { left: 0; top: 12px; width: 100%; transform: skewY(-2deg); }
  .window.right .window-band { left: 0; top: 18px; width: 100%; transform: skewY(-1deg); }

  .walkin-badge {
    position: absolute; left: 620px; top: 464px; width: 140px; height: 140px; border-radius: 50%;
    background: var(--ink); color: var(--paper); text-align: center;
    display: flex; flex-direction: column; align-items: center; justify-content: center;
  }
  .walkin-yes { font-size: 48px; font-weight: 500; line-height: 1; }
  .walkin-line { font-size: 20px; line-height: 1.1; margin-top: 4px; }
  .walkin-who { font-size: 10.5px; line-height: 1.2; }
</style>
</head>
<body>
<main class="shopfront">
  <div class="fascia timber" role="img" aria-label="Timber fascia board"></div>
  <div class="fascia-band">
    <span class="fascia-dot"></span>
    <span class="fascia-name">Crisp Vintage Hair</span>
  </div>

  <div class="pillar timber" role="img" aria-label="Timber side pillar"></div>
  <div class="pillar-name">Crisp<br>Vintage<br>Hair</div>
  <ul class="service-list">
    <li>Ladies</li><li>Men</li><li>Children</li><li>Styles</li><li>Cut</li>
    <li>Colour</li><li>Blowdry</li><li>Upstyle</li><li>Perm</li><li>Treatment</li>
  </ul>

  <div class="frame"></div>
  <p class="frame-text phone">Call: 0000 000 000</p>
  <p class="frame-text web">www.crispvintagehair.com</p>

  <div class="window left" role="img" aria-label="Shop window showing styling stations"><span class="window-band"></span></div>
  <div class="window right" role="img" aria-label="Shop window showing salon interior and retail shelves"><span class="window-band"></span></div>

  <div class="walkin-badge">
    <span class="walkin-yes">Yes</span>
    <span class="walkin-line">we take walk in’s</span>
    <span class="walkin-who">men - women - children</span>
  </div>
</main>
</body>
</html>
```